Harrow Glen Whiskey Label

We are looking for a label to be made for our single batch whiskey. in the attached pdf you will see the lay out of the design. We are going to use a whiskey bottle with a cork. Some of the label you will need to leave some space for hand writing.

Target Market(s)

people who like craft beer and whiskey

Industry/Entity Type

Craft Distillery

Font styles to use
Decorative

Colors

Designer to choose colors to be used in the design.

Requirements
Must have
• room for hand writing informatiom

```html
<!DOCTYPE html>
<html lang="en">
<head>
<meta charset="utf-8">
<title>Harrow Glen Whiskey Label</title>
<link rel="stylesheet" href="https://fonts.googleapis.com/css2?family=Crimson+Text:wght@400;600;700&family=Open+Sans:wght@400;700&family=Parisienne&family=Courier+Prime:wght@700&display=swap">
<style>
  :root {
    --canvas: #c5c3c4;
    --label-brown: #43271a;
    --label-edge: #ffffff;
    --ink-light: #ffffff;
    --ornament: #8a5a30;
    --ornament-soft: #b39684;
    --field: #ffffff;
    --field-ink: #2a1a12;
  }
  * { margin: 0; padding: 0; box-sizing: border-box; }
  html, body { width: 1200px; height: 1200px; overflow: hidden; background: var(--canvas); }
  .canvas { position: relative; width: 1200px; height: 1200px; }
  .label {
    position: absolute; left: 329px; top: 170px; width: 543px; height: 860px;
    background: var(--label-brown);
    border: 6px solid var(--label-edge);
    border-radius: 62px 62px 76px 76px;
    overflow: hidden;
    color: var(--ink-light);
  }
  .label > * { position: absolute; }
  .ornament { border-radius: 40% 60% 50% 50%; }
  .ornament--crest { left: 174px; top: 12px; width: 180px; height: 62px; background: var(--ornament-soft); opacity: .55; border-radius: 50% 50% 30% 30%; }
  .ornament--scroll { left: 162px; top: 222px; width: 206px; height: 56px; background: var(--ornament-soft); opacity: .55; border-radius: 30% 30% 50% 50%; }
  .ornament--leaf { width: 44px; height: 70px; background: var(--ornament); opacity: .7; }
  .leaf-tl { left: 4px; top: 4px; }
  .leaf-tr { right: 6px; top: 8px; }
  .leaf-ml { left: 14px; top: 326px; }
  .leaf-mr { right: 14px; top: 340px; }
  .leaf-rr { right: 2px; top: 540px; height: 56px; }
  .leaf-br { right: 8px; top: 680px; height: 56px; }
  .leaf-bl { left: 20px; top: 760px; }
  .brand-name {
    left: 0; width: 100%; text-align: center;
    font-family: "Crimson Text", serif; font-weight: 700; font-size: 62px; line-height: 1;
    color: var(--ink-light);
  }
  .brand-name--top { top: 90px; }
  .brand-name--bottom { top: 166px; }
  .rule { left: 115px; width: 313px; height: 12px; }
  .rule--upper { top: 285px; }
  .rule--lower { top: 343px; }
  .product-name {
    left: 0; width: 100%; top: 296px; text-align: center;
    font-family: "Parisienne", cursive; font-size: 44px; line-height: 1;
  }
  .spirit-line {
    left: 0; width: 100%; text-align: center;
    font-family: "Crimson Text", serif; font-weight: 600;
  }
  .spirit-line--small { top: 374px; font-size: 23px; }
  .spirit-line--large { top: 408px; font-size: 31px; }
  .field {
    background: var(--field); border-radius: 14px;
    font-family: "Crimson Text", serif; font-size: 19px; color: var(--field-ink);
    padding: 6px 9px;
  }
  .field--source { left: 58px; top: 458px; width: 435px; height: 47px; padding-top: 10px; }
  .field--aged { left: 58px; top: 522px; width: 207px; height: 87px; }
  .field--abv { left: 286px; top: 522px; width: 209px; height: 87px; padding-left: 14px; font-size: 17px; }
  .field--bottle { left: 58px; top: 624px; width: 210px; height: 83px; border-radius: 14px 0 0 14px; padding-left: 12px; }
  .field--of { left: 274px; top: 624px; width: 219px; height: 83px; border-radius: 0 14px 14px 0; padding-left: 17px; }
  .maker {
    left: 0; width: 100%; text-align: center;
    font-family: "Open Sans", sans-serif; line-height: 1;
  }
  .maker--intro { top: 728px; font-size: 17px; }
  .maker--name { top: 752px; font-size: 21px; font-weight: 700; }
  .maker--address { top: 780px; font-size: 18px; }
  .volume {
    right: 40px; top: 818px;
    font-family: "Courier Prime", monospace; font-weight: 700; font-size: 19px;
  }
</style>
</head>
<body>
<main class="canvas">
  <section class="label">
    <div class="ornament ornament--leaf leaf-tl" role="img" aria-label="Corner flourish ornament"></div>
    <div class="ornament ornament--leaf leaf-tr" role="img" aria-label="Corner flourish ornament"></div>
    <div class="ornament ornament--leaf leaf-ml" role="img" aria-label="Side flourish ornament"></div>
    <div class="ornament ornament--leaf leaf-mr" role="img" aria-label="Side flourish ornament"></div>
    <div class="ornament ornament--leaf leaf-rr" role="img" aria-label="Side flourish ornament"></div>
    <div class="ornament ornament--leaf leaf-br" role="img" aria-label="Side flourish ornament"></div>
    <div class="ornament ornament--leaf leaf-bl" role="img" aria-label="Corner flourish ornament"></div>
    <div class="ornament ornament--crest" role="img" aria-label="Decorative scroll crest above the name"></div>

    <h1 class="brand-name brand-name--top">Ironbend</h1>
    <p class="brand-name brand-name--bottom">Distillery</p>

    <div class="ornament ornament--scroll" role="img" aria-label="Decorative scroll beneath the name"></div>

    <svg class="rule rule--upper" viewBox="0 0 313 12" aria-hidden="true">
      <line x1="8" y1="6" x2="305" y2="6" stroke="#fff" stroke-width="1.5"/>
      <circle cx="6" cy="6" r="3" fill="none" stroke="#fff" stroke-width="1.2"/>
      <circle cx="307" cy="6" r="3" fill="none" stroke="#fff" stroke-width="1.2"/>
      <circle cx="156.5" cy="6" r="3.5" fill="#43271a" stroke="#fff" stroke-width="1.2"/>
    </svg>
    <h2 class="product-name">Harrow Glen</h2>
    <svg class="rule rule--lower" viewBox="0 0 313 12" aria-hidden="true">
      <line x1="8" y1="6" x2="305" y2="6" stroke="#fff" stroke-width="1.5"/>
      <circle cx="6" cy="6" r="3" fill="none" stroke="#fff" stroke-width="1.2"/>
      <circle cx="307" cy="6" r="3" fill="none" stroke="#fff" stroke-width="1.2"/>
      <circle cx="156.5" cy="6" r="3.5" fill="#43271a" stroke="#fff" stroke-width="1.2"/>
    </svg>

    <p class="spirit-line spirit-line--small">Spirits Distilled from</p>
    <p class="spirit-line spirit-line--large">Malt Mash and Hops</p>

    <div class="field field--source">Distilate Source:</div>
    <div class="field field--aged">Aged:</div>
    <div class="field field--abv">% Alc. by Vol.</div>
    <div class="field field--bottle">Bottle:</div>
    <div class="field field--of">Of:</div>

    <p class="maker maker--intro">DISTILLED AND BOTTLED BY</p>
    <p class="maker maker--name">IRONBEND DISTILLERY LLC</p>
    <p class="maker maker--address">48 FOUNDRY LANE MILLBROOK NJ 08017</p>
    <p class="volume">750ML</p>
  </section>
</main>
</body>
</html>
```